Industrial Automation company requires a business card design

Valtrin Automation provides design & build of Automated Equipment for manufacturing industry.
www.valtrinautomation.example
The equipment we design is used for manufacturing in sectors such as medical device, pharmaceutical, aerospace and electronics.
We require a new business card design which incorporates our (New) logo and the key message words:
Automated Equipment:
Design, Build, Control, Test, Support

```html
<!DOCTYPE html>
<html lang="en">
<head>
<meta charset="utf-8">
<title>Valtrin Automation – Business Card</title>
<link rel="stylesheet" href="https://fonts.googleapis.com/css2?family=Arimo:wght@400;700&display=swap">
<style>
  :root {
    --backdrop: #e6e6e3;
    --card: #ffffff;
    --brand-green: #17843a;
    --ink: #2b2b2b;
  }
  * { box-sizing: border-box; margin: 0; padding: 0; }
  html, body { width: 1200px; height: 873px; overflow: hidden; }
  body {
    background: var(--backdrop);
    font-family: "Arimo", Arial, sans-serif;
    color: var(--ink);
    position: relative;
  }
  .card {
    position: absolute;
    top: 156px;
    width: 340px;
    height: 560px;
    background: var(--card);
    box-shadow: 0 10px 30px rgba(0,0,0,0.12);
    overflow: hidden;
  }
  .card--front { left: 190px; }
  .card--back { left: 670px; }

  /* Front */
  .brand-lockup {
    position: absolute;
    left: 40px;
    right: 40px;
    top: 236px;
    display: flex;
    align-items: center;
    justify-content: center;
    gap: 10px;
  }
  .brand-lockup__mark {
    flex: none;
    width: 14px; height: 14px;
    background: var(--brand-green);
  }
  .brand-lockup__name {
    font-weight: 700;
    font-size: 19px;
    letter-spacing: 0.5px;
    color: var(--brand-green);
    white-space: nowrap;
  }
  .key-message {
    position: absolute;
    right: 26px;
    bottom: 34px;
    text-align: right;
    font-size: 13px;
    color: var(--ink);
    line-height: 1.9;
  }
  .key-message__list .sep { margin: 0 6px; }

  /* Back */
  .contact {
    position: absolute;
    left: 34px;
    top: 44px;
  }
  .contact__name {
    font-weight: 700;
    font-size: 22px;
    color: var(--brand-green);
  }
  .rule {
    display: block;
    width: 20px;
    height: 3px;
    background: var(--brand-green);
    margin: 10px 0;
  }
  .contact__details, .location {
    font-size: 13px;
    line-height: 1.55;
    color: var(--ink);
  }
  .location {
    position: absolute;
    left: 132px;
    top: 300px;
  }
  .back-brand {
    position: absolute;
    right: 26px;
    bottom: 30px;
    display: flex;
    align-items: center;
    gap: 6px;
  }
  .back-brand__mark {
    width: 8px; height: 8px;
    background: var(--brand-green);
  }
  .back-brand__name {
    font-weight: 700;
    font-size: 11px;
    letter-spacing: 0.5px;
    color: var(--brand-green);
  }
</style>
</head>
<body>
  <section class="card card--front" aria-label="Business card front">
    <div class="brand-lockup">
      <span class="brand-lockup__mark"></span>
      <span class="brand-lockup__name">VALTRIN AUTOMATION</span>
    </div>
    <div class="key-message">
      <p class="key-message__title">Automated Equipment :</p>
      <p class="key-message__list">Design<span class="sep">|</span>Build<span class="sep">|</span>Control<span class="sep">|</span>Test<span class="sep">|</span>Support</p>
    </div>
  </section>

  <section class="card card--back" aria-label="Business card back">
    <div class="contact">
      <h1 class="contact__name">Your Name</h1>
      <span class="rule"></span>
      <p class="contact__details">
        Position Name<br>
        012 - 345 - 6789<br>
        info@valtrinautomation.example
      </p>
    </div>
    <div class="location">
      <p>Mon - Fri<br>9:00 - 17:00</p>
      <span class="rule"></span>
      <p>100 Address Street<br>Town/City<br>Province<br>01A 2BC</p>
    </div>
    <div class="back-brand">
      <span class="back-brand__mark"></span>
      <span class="back-brand__name">VALTRIN AUTOMATION</span>
    </div>
  </section>
</body>
</html>
```